Business Card Design

I need a business card designed for my new company BrightOak Home developments I specialise in all aspects of carpentry including Decks, Pergolas, Conventional Framing and fit outs I am open to different colours as long as it fits with my logo.

Industry/Entity Type

Carpentry

Contact Information for Business Card

BrightOak Home Developments, Greg Mollory, 0461802394, specialising in all aspects of carpentry and construction

```html
<!DOCTYPE html>
<html lang="en">
<head>
<meta charset="utf-8">
<title>BrightOak Home Developments – Business Card</title>
<link rel="stylesheet" href="https://fonts.googleapis.com/css2?family=Exo+2:wght@400;500&family=Open+Sans:wght@400&display=swap">
<style>
  :root {
    --stage: #2a2a2c;
    --card-blue: #2d5fb0;
    --card-blue-edge: #2a58a6;
    --honeycomb: #3f3a35;
    --ink-dark: #2c3340;
    --ink-light: #ffffff;
    --contact: #8fa3c4;
    --rule-gold: #b39a6a;
  }
  * { margin: 0; padding: 0; box-sizing: border-box; }
  html, body {
    width: 1200px;
    height: 816px;
    overflow: hidden;
    background: var(--stage);
  }
  .card {
    position: absolute;
    left: 80px;
    top: 98px;
    width: 1040px;
    height: 620px;
    border-radius: 44px;
    overflow: hidden;
    border: 8px solid var(--card-blue-edge);
    background: var(--honeycomb);
  }
  .card__texture {
    position: absolute;
    inset: 0;
    background: linear-gradient(135deg, #443e38 0%, var(--honeycomb) 55%, #3a3531 100%);
  }
  .card__shapes {
    position: absolute;
    inset: 0;
    width: 100%;
    height: 100%;
  }
  .brand {
    position: absolute;
    left: 190px;
    top: 110px;
    width: 430px;
    display: flex;
    align-items: center;
    gap: 18px;
    color: var(--ink-light);
    font-family: "Exo 2", sans-serif;
    font-weight: 500;
    font-size: 30px;
    line-height: 1.15;
    letter-spacing: 1px;
  }
  .brand__mark {
    width: 26px;
    height: 26px;
    flex: none;
    background: var(--ink-light);
  }
  .person {
    position: absolute;
    right: 500px;
    top: 398px;
    text-align: right;
    font-family: "Exo 2", sans-serif;
    font-weight: 500;
    color: var(--ink-dark);
  }
  .person__name {
    font-size: 40px;
    letter-spacing: 2px;
    line-height: 1;
  }
  .person__role {
    font-size: 22px;
    letter-spacing: 1.5px;
    margin-top: 6px;
  }
  .divider {
    position: absolute;
    left: 556px;
    top: 282px;
    width: 2px;
    height: 160px;
    background: var(--rule-gold);
  }
  .contact {
    position: absolute;
    left: 576px;
    top: 288px;
    list-style: none;
    font-family: "Open Sans", sans-serif;
    font-size: 17px;
    line-height: 30px;
    color: var(--contact);
    letter-spacing: 0.5px;
  }
</style>
</head>
<body>
  <div class="card">
    <div class="card__texture" role="img" aria-label="Dark honeycomb pattern with thin gold hexagon outlines"></div>

    <svg class="card__shapes" viewBox="0 0 1024 604" aria-hidden="true">
      <!-- top tab -->
      <path fill="var(--card-blue)"
        d="M110,0 C140,0 150,14 150,44 L150,222 Q150,262 190,262 L610,262 Q650,262 650,222 L650,44 C650,14 660,0 690,0 Z"/>
      <!-- main band -->
      <rect fill="var(--card-blue)" x="0" y="378" width="1024" height="120"/>
    </svg>

    <div class="brand">
      <span class="brand__mark"></span>
      <span class="brand__name">BrightOak<br>Home Developments</span>
    </div>

    <div class="person">
      <div class="person__name">Greg Mollory</div>
      <div class="person__role">Director &amp; CEO</div>
    </div>

    <div class="divider"></div>

    <ul class="contact">
      <li>0461 802 394</li>
      <li>greg@brightoakhomes.com</li>
      <li>brightoakhomes.com</li>
    </ul>
  </div>
</body>
</html>
```